Consulting & Education Company Needs Dynamic MS Word Template

We need a MS Word Template for everyday documents. This would be leveraged to create reports, marketing materials, internal memos etc.

The document should follow the standard MS Word template format and have an H1,H2,H3, paragraph, Title, bold font, regular font, table etc. All editable with normal MS Word features.

Attached is a Logo which was created by one of the many talented folks here at Brightfold. We would like to see the same color scheme used throughout the document. Additional attached is a sample word document that outlines all of the components we would like to see in the template.

Target Market(s)

Information Security - Penetration Testing - IT - Network/Systems Engineering

Industry/Entity Type

Education

Requirements
Must have
• Submission must meet all standard MS Word Template requirements.
• Submission should make use of Built in MS Styles so as the user of the template I shoudl be able to create a brand new page and insert an H1 for example and be able to select from the styles drop down the same font/color/style that you have designed for your submission.
• All sections in the provided document need to be contained in your submission.
• The table of contents should auto update if I add a new page, heading, section etc.
• Need to read and understand all of my comments which I have placed in the sample document uploaded to the briefing
Nice to have
• the cover page should be eye catching but not over the top. Some cool vectors/bg colors etc that look nice with the logo already provided.
• Icons and vectors whever they make sense and are visually appealing. For example the document has a section for defiing severity risk: Critical, High, Medium and Low it would be great if there was a nice icon or 2d graphic associated with each one. also color coded is a plus High is more dangerous then medium so the colors should communicate that.
Should not have
• no fixed textboxes or image boxes. everything needs to be smoothly editable in MS Word. "Editable" means more than just being able to alter text.

```html
<!DOCTYPE html>
<html lang="en">
<head>
<meta charset="utf-8">
<title>Ironquill Report Template</title>
<link href="https://fonts.googleapis.com/css2?family=Montserrat:wght@500;600;700&family=Open+Sans:wght@400;600;700&display=swap" rel="stylesheet">
<style>
:root{
  --red:#d71920;--ink:#1b1b1b;--slate:#37414a;--tag:#5e5e5e;--tag-dark:#4a4a4a;
  --light:#ececec;--lighter:#f5f5f5;--bg:#d2d2d2;--text:#3a3a3a;
  --crit:#3a2f26;--high:#d71920;--med:#f5a623;--low:#1aa3d4;
}
*{box-sizing:border-box;margin:0;padding:0}
html,body{width:904px;height:1200px;overflow:hidden;background:var(--bg)}
.sheet{width:904px;height:1200px;display:grid;grid-template-columns:repeat(4,1fr);grid-template-rows:repeat(4,1fr);gap:8px;padding:4px;background:var(--bg)}
.page{position:relative;background:#fff;overflow:hidden;font-family:'Open Sans',sans-serif;color:var(--text)}
.brand{position:absolute;top:10px;right:12px;display:flex;align-items:center;gap:2px}
.brand-mark{width:6px;height:6px;background:var(--red);border-radius:50%}
.brand-name{font-family:'Montserrat',sans-serif;font-weight:700;font-size:6px;color:var(--red);letter-spacing:.2px}
.foot-left{position:absolute;left:0;bottom:0;width:96px;height:11px;background:var(--red);clip-path:polygon(0 0,88% 0,100% 100%,0 100%);font-size:3.2px;color:#fff;font-weight:600;padding:4px 0 0 8px;word-spacing:3px}
.foot-edge{position:absolute;left:0;bottom:10px;width:26px;height:6px;background:var(--ink);clip-path:polygon(0 0,55% 0,100% 100%,0 100%)}
.foot-right{position:absolute;right:0;bottom:0;width:52px;height:11px;background:var(--red);clip-path:polygon(24% 0,100% 0,100% 100%,0 100%);font-size:3.6px;color:#fff;text-align:right;padding:3.5px 9px 0 0}
.foot-right-edge{position:absolute;right:0;bottom:10px;width:16px;height:9px;background:var(--ink);clip-path:polygon(100% 0,100% 100%,0 100%)}
.body{position:absolute;left:24px;right:24px;top:40px}
.h-red{font-family:'Montserrat',sans-serif;font-weight:600;font-size:10px;color:var(--red);margin-bottom:3px}
.h-dark{font-family:'Montserrat',sans-serif;font-weight:600;font-size:8.5px;color:var(--ink);margin-bottom:3px}
.h-small{font-family:'Montserrat',sans-serif;font-weight:600;font-size:7px;color:var(--ink);line-height:1.05}
.para{font-size:3.6px;line-height:1.4;margin-bottom:7px}
table{width:100%;border-collapse:collapse;font-size:3.4px}
/* cover */
.cover-brand{position:absolute;top:30px;left:22px;display:flex;align-items:center;gap:3px}
.cover-brand .brand-mark{width:13px;height:13px}
.cover-brand .brand-name{font-size:11px}
.cover-title{position:absolute;top:78px;left:0;width:176px;height:50px;background:var(--red);clip-path:polygon(0 0,100% 0,82% 100%,0 100%);padding:9px 0 0 22px;color:#fff;font-family:'Montserrat',sans-serif}
.cover-title .client{font-size:8.5px;font-weight:500}
.cover-title .title{font-size:12.5px;font-weight:700;margin-top:1px}
.cover-date{position:absolute;top:136px;left:0;width:102px;height:18px;background:var(--slate);clip-path:polygon(0 0,100% 0,86% 100%,0 100%);color:#fff;font-size:4.6px;font-weight:600;padding:6.5px 0 0 22px}
.cover-art{position:absolute;right:0;bottom:0;width:140px;height:96px;background:linear-gradient(135deg,#fff 10%,#f7dadb 100%)}
/* toc */
.toc{position:absolute;top:70px;left:24px;right:24px;font-size:3.3px;color:#333}
.toc-row{display:flex;align-items:flex-end;line-height:1.55}
.toc-row.main{font-weight:700;margin-top:6px}
.toc-row.lvl2{padding-left:0}
.toc-row.lvl3{padding-left:3px}
.toc-row.lvl4{padding-left:7px}
.toc-dots{flex:1;border-bottom:.5px dotted #555;margin:0 1px 1px}
/* scope table */
.scope-table{background:var(--slate);color:#fff;margin:4px 0 8px}
.scope-table th{height:11px;font-weight:700;font-size:3.6px}
.scope-table th.red{background:var(--red)}
.scope-table th.grey{background:#9aa0a6}
.scope-table td{height:8px;text-align:center;border-top:.5px solid #566069}
.scope-table td:first-child{text-align:left;padding-left:5px;width:26%}
/* observations table */
.obs-table{margin-top:5px}
.obs-table th{background:var(--slate);color:#fff;height:11px;font-weight:600}
.obs-table th:first-child{background:#9aa0a6}
.obs-table td{height:8px;text-align:center;background:var(--light);border-top:.5px solid #fff;color:#444}
.obs-table td:first-child{text-align:left;padding-left:3px;background:#dedede}
/* severity ratings */
.sev-table th{background:#000;color:#fff;height:16px;text-align:left;padding-left:6px;font-weight:700}
.sev-table td{padding:4px 4px;vertical-align:middle;line-height:1.35;font-size:3.3px}
.sev-table tr:nth-child(even) td{background:var(--light)}
.sev-table tr:nth-child(odd) td{background:var(--lighter)}
.sev-cell{display:flex;align-items:center;gap:3px;font-weight:600;width:44px}
.sev-cell svg{width:6px;height:6px}
.t-crit{color:#444}.t-high{color:var(--high)}.t-med{color:var(--med)}.t-low{color:var(--low)}
/* findings summary */
.find-table{margin-top:14px;background:var(--light)}
.find-table caption{background:var(--red);color:#fff;text-align:left;font-family:'Montserrat',sans-serif;font-weight:700;font-size:5px;padding:6px 0 6px 10px;border-bottom:4px solid #b51218}
.find-table th{background:var(--slate);color:#fff;height:14px;text-align:left;padding-left:8px;font-weight:600}
.find-table th+th{border-left:1px solid #fff;text-align:center;padding:0}
.find-table td{height:11px;padding-left:8px;font-size:3.2px}
.find-table td+td{text-align:center;padding:0;border-left:1px solid #fff}
/* finding card */
.finding-title{position:absolute;top:40px;left:22px}
.finding{position:absolute;top:56px;left:22px;right:22px;font-size:3.4px}
.f-head{display:flex;height:20px}
.f-name{width:40px;background:#111;color:#fff;font-weight:700;font-size:3.6px;line-height:1.05;display:flex;align-items:center;justify-content:center;text-align:center;padding:0 2px}
.f-sev-label{flex:1;background:var(--tag-dark);color:#fff;font-weight:600;display:flex;align-items:center;justify-content:center}
.f-sev{width:45%;color:#fff;font-weight:600;display:flex;align-items:center;justify-content:center}
.f-sev.crit{background:var(--crit)}.f-sev.high{background:var(--high)}.f-sev.med{background:var(--med)}.f-sev.low{background:var(--low)}
.f-row{display:flex}
.f-tag{width:40px;background:var(--tag);color:#fff;font-weight:600;font-size:3.5px;display:flex;flex-direction:column;align-items:center;justify-content:center;gap:1px}
.f-tag svg{width:7px;height:7px}
.f-text{flex:1;padding:2px 2px;line-height:1.35;color:#333}
.obs .f-text,.rec .f-text{background:var(--light)}
.obs{height:24px}.ev{height:77px}.rec{height:40px}.assets{height:23px}
.ev .f-text{background:#fff;display:flex;flex-direction:column;align-items:center;justify-content:center}
.shot{width:72px;height:60px;background:linear-gradient(180deg,#f2f2f2,#dcdfe4);border:.5px solid #bbb}
.caption{margin-top:3px;font-size:3px}
.f-text ul{padding-left:8px;margin-top:1px}
.assets .f-text{background:var(--lighter)}
.assets ul{list-style:disc}
/* contact */
.contact-photo{position:absolute;top:58px;left:24px;right:24px;height:116px;background:linear-gradient(160deg,#f4f4f4,#bdbdbd 60%,#8a8a8a)}
.contact-list{position:absolute;top:182px;left:24px;right:24px}
.contact-item{display:flex;gap:3px;margin-bottom:4px}
.c-icon{width:7px;height:7px;border-radius:50%;background:var(--red);display:flex;align-items:center;justify-content:center;flex:none}
.c-icon svg{width:4px;height:4px}
.c-label{font-size:4.2px;font-weight:700;color:var(--red);line-height:1.2}
.c-value{font-size:3.3px;color:#333}
</style>
</head>
<body>
<main class="sheet">

<!-- 1 cover -->
<section class="page">
  <div class="cover-brand"><span class="brand-mark"></span><span class="brand-name">IRONQUILL</span></div>
  <div class="cover-title"><div class="client">Client Name</div><div class="title">Engagement Title</div></div>
  <div class="cover-date">Month Day, Year</div>
  <div class="cover-art" role="img" aria-label="Red network of connected polygon lines"></div>
</section>

<!-- 2 contents -->
<section class="page">
  <div class="brand"><span class="brand-mark"></span><span class="brand-name">IRONQUILL</span></div>
  <div class="toc">
    <div class="toc-row main"><span>ENGAGEMENT OVERVIEW</span><span class="toc-dots"></span><span>2</span></div>
    <div class="toc-row"><span>Engagement Scope</span><span class="toc-dots"></span><span>2</span></div>
    <div class="toc-row"><span>Engagement Summary</span><span class="toc-dots"></span><span>3</span></div>
    <div class="toc-row"><span>Key Observations</span><span class="toc-dots"></span><span>3</span></div>
    <div class="toc-row main"><span>TECHNICAL OVERVIEW</span><span class="toc-dots"></span><span>4</span></div>
    <div class="toc-row"><span>Severity Ratings</span><span class="toc-dots"></span><span>4</span></div>
    <div class="toc-row"><span>Summary Of Findings</span><span class="toc-dots"></span><span>5</span></div>
    <div class="toc-row"><span>Detailed Observations</span><span class="toc-dots"></span><span>6</span></div>
    <div class="toc-row lvl3"><span>Critical Finding</span><span class="toc-dots"></span><span>6</span></div>
    <div class="toc-row lvl4"><span>Insecure Configurations Identified</span><span class="toc-dots"></span><span>6</span></div>
    <div class="toc-row lvl4"><span>Missing Patches</span><span class="toc-dots"></span><span>7</span></div>
    <div class="toc-row lvl3"><span>High Finding</span><span class="toc-dots"></span><span>8</span></div>
    <div class="toc-row lvl4"><span>Insecure Configurations Identified</span><span class="toc-dots"></span><span>8</span></div>
    <div class="toc-row lvl4"><span>Missing Patches</span><span class="toc-dots"></span><span>9</span></div>
    <div class="toc-row lvl3"><span>Medium Finding</span><span class="toc-dots"></span><span>10</span></div>
    <div class="toc-row lvl4"><span>Insecure Configurations Identified</span><span class="toc-dots"></span><span>10</span></div>
    <div class="toc-row lvl4"><span>Missing Hardening Checks</span><span class="toc-dots"></span><span>11</span></div>
    <div class="toc-row lvl3"><span>Low Finding</span><span class="toc-dots"></span><span>12</span></div>
    <div class="toc-row lvl4"><span>Insecure Configurations Identified</span><span class="toc-dots"></span><span>12</span></div>
    <div class="toc-row lvl4"><span>Missing Hardening Checks</span><span class="toc-dots"></span><span>13</span></div>
    <div class="toc-row main"><span>APPENDIX 01</span><span class="toc-dots"></span><span>14</span></div>
    <div class="toc-row"><span>Engagement Methodology</span><span class="toc-dots"></span><span>14</span></div>
    <div class="toc-row main"><span>OUR CONTACT</span><span class="toc-dots"></span><span>15</span></div>
  </div>
  <div class="foot-edge"></div><div class="foot-left">Client Name Engagement Title</div>
  <div class="foot-right-edge"></div><div class="foot-right">1</div>
</section>

<!-- 3 overview -->
<section class="page">
  <div class="brand"><span class="brand-mark"></span><span class="brand-name">IRONQUILL</span></div>
  <div class="body">
    <h1 class="h-red">Engagement Overview</h1>
    <p class="para">This report summarises the security assessment carried out for the client, outlining goals, methods and the key results so readers can grasp the overall risk and the next steps to improve the security posture.</p>
    <h2 class="h-dark">Engagement Scope</h2>
    <p class="para">The scope covered external and internal hosts, web applications and user workstations agreed with the client before testing began.</p>
    <table class="scope-table">
      <tr><th></th><th class="red">Column 1</th><th class="grey">Column 2</th><th class="red">Column 3</th></tr>
      <tr><td>Description 1</td><td>1</td><td>2</td><td>3</td></tr>
      <tr><td>Description 2</td><td>Text 1</td><td>Text 2</td><td>Text 3</td></tr>
      <tr><td>Description 3</td><td>• Bullet 1a</td><td>• Bullet 2a</td><td>• Bullet 3a</td></tr>
      <tr><td>Description 4</td><td>• Bullet 1b</td><td>• Bullet 2b</td><td>• Bullet 3b</td></tr>
    </table>
    <p class="para">All testing took place in the agreed window, and every system listed above was reviewed using the same methodology and tooling.</p>
  </div>
  <div class="foot-edge"></div><div class="foot-left">Client Name Engagement Title</div>
  <div class="foot-right-edge"></div><div class="foot-right">2</div>
</section>

<!-- 4 summary -->
<section class="page">
  <div class="brand"><span class="brand-mark"></span><span class="brand-name">IRONQUILL</span></div>
  <div class="body">
    <h2 class="h-dark">Engagement Summary</h2>
    <p class="para">Across the engagement, several weaknesses were found that could let an attacker gain a foothold. Most issues stem from outdated software and weak default settings that can be fixed with modest effort and clear ownership across the affected teams.</p>
    <h2 class="h-dark">Key Observations</h2>
    <p class="para">The table below lists the main observations, grouped by area, with counts that show where remediation should be focused first.</p>
    <table class="obs-table">
      <tr><th></th><th>Column 1</th><th>Column 2</th><th>Column 3</th><th>Column 4</th></tr>
      <tr><td>Description 1</td><td>Text</td><td>Text</td><td>Text</td><td>Text</td></tr>
      <tr><td>Description 2</td><td>Number 1</td><td>Number 2</td><td>Number 3</td><td>Number 4</td></tr>
      <tr><td>Description 3</td><td>Text</td><td>Text</td><td>Text</td><td>Text</td></tr>
      <tr><td>Description 4</td><td>Number 1</td><td>Number 2</td><td>Number 3</td><td>Number 4</td></tr>
    </table>
  </div>
  <div class="foot-edge"></div><div class="foot-left">Client Name Engagement Title</div>
  <div class="foot-right-edge"></div><div class="foot-right">3</div>
</section>

<!-- 5 technical -->
<section class="page">
  <div class="brand"><span class="brand-mark"></span><span class="brand-name">IRONQUILL</span></div>
  <div class="body">
    <h1 class="h-red">Technical Overview</h1>
    <p class="para">This section explains how findings are rated and presents each issue with evidence, recommended fixes and the assets affected.</p>
    <h2 class="h-dark">Severity Ratings</h2>
    <table class="sev-table">
      <tr><th>Severity</th><th>Description</th></tr>
      <tr><td><div class="sev-cell t-crit"><svg viewBox="0 0 6 6"><rect x="0" y="4" width="1.4" height="2" fill="#444"/><rect x="2.2" y="2" width="1.4" height="4" fill="#444"/><rect x="4.4" y="0" width="1.4" height="6" fill="#444"/></svg>Critical</div></td><td>Immediate threat that allows full system compromise and must be fixed without delay.</td></tr>
      <tr><td><div class="sev-cell t-high"><svg viewBox="0 0 6 6"><rect x="0" y="4" width="1.4" height="2" fill="#d71920"/><rect x="2.2" y="2" width="1.4" height="4" fill="#d71920"/><rect x="4.4" y="0" width="1.4" height="6" fill="#e8a0a3"/></svg>High</div></td><td>Serious weakness that can lead to data loss and should be fixed promptly.</td></tr>
      <tr><td><div class="sev-cell t-med"><svg viewBox="0 0 6 6"><rect x="0" y="4" width="1.4" height="2" fill="#f5a623"/><rect x="2.2" y="2" width="1.4" height="4" fill="#fbd9a0"/><rect x="4.4" y="0" width="1.4" height="6" fill="#fbd9a0"/></svg>Medium</div></td><td>Moderate risk that needs specific conditions to exploit and should be planned.</td></tr>
      <tr><td><div class="sev-cell t-low"><svg viewBox="0 0 6 6"><circle cx="3" cy="3" r="2.6" fill="none" stroke="#1aa3d4" stroke-width=".8"/><path d="M1.8 3.1l.9.9 1.6-1.9" fill="none" stroke="#1aa3d4" stroke-width=".7"/></svg>Low</div></td><td>Minor issue with limited impact that can be addressed during routine upkeep.</td></tr>
    </table>
  </div>
  <div class="foot-edge"></div><div class="foot-left">Client Name Engagement Title</div>
  <div class="foot-right-edge"></div><div class="foot-right">4</div>
</section>

<!-- 6 findings summary -->
<section class="page">
  <div class="brand"><span class="brand-mark"></span><span class="brand-name">IRONQUILL</span></div>
  <div class="body">
    <h2 class="h-dark">Summary Of Findings</h2>
    <p class="para">Each finding below is listed with its assigned severity to help prioritise remediation work.</p>
    <table class="find-table">
      <caption>Table 3</caption>
      <tr><th>Finding Name</th><th>Severity</th></tr>
      <tr><td>Critical Finding Title</td><td>Critical</td></tr>
      <tr><td class="t-high">High Finding Title</td><td class="t-high">High</td></tr>
      <tr><td class="t-med">Medium Finding Title</td><td class="t-med">Medium</td></tr>
      <tr><td class="t-low">Low Finding Title</td><td class="t-low">Low</td></tr>
    </table>
  </div>
  <div class="foot-edge"></div><div class="foot-left">Client Name Engagement Title</div>
  <div class="foot-right-edge"></div><div class="foot-right">5</div>
</section>

<!-- finding pages -->
<section class="page">
  <div class="brand"><span class="brand-mark"></span><span class="brand-name">IRONQUILL</span></div>
  <div class="finding-title"><div class="h-small">Detailed Observations</div><div class="h-small">Critical Finding</div></div>
  <div class="finding" style="top:58px">
    <div class="f-head"><div class="f-name">Insecure Configurations Identified</div><div class="f-sev-label">Severity</div><div class="f-sev crit">Critical</div></div>
    <div class="f-row obs"><div class="f-tag"><svg viewBox="0 0 8 8"><circle cx="3.3" cy="3.3" r="2.3" fill="none" stroke="#fff" stroke-width=".9"/><path d="M5 5l2.3 2.3" stroke="#fff" stroke-width="1"/></svg>Observation</div><div class="f-text">Several hosts expose services with default settings, allowing unauthorised users to view sensitive details and change system behaviour.</div></div>
    <div class="f-row ev"><div class="f-tag"><svg viewBox="0 0 8 8"><rect x="1" y="2.5" width="6" height="4.5" fill="none" stroke="#fff" stroke-width=".8"/><path d="M3 2.5V1.5h2v1" fill="none" stroke="#fff" stroke-width=".8"/></svg>Evidence</div><div class="f-text"><div class="shot" role="img" aria-label="Screenshot of scan results"></div><p class="caption">Figure #1 - This is a caption for the above screenshot</p></div></div>
    <div class="f-row rec"><div class="f-tag"><svg viewBox="0 0 8 8"><rect x="1.5" y="1.2" width="5" height="6.3" fill="none" stroke="#fff" stroke-width=".8"/><path d="M2.8 3.3h2.4M2.8 4.7h2.4" stroke="#fff" stroke-width=".6"/></svg>Recommendation</div><div class="f-text">Apply a secure baseline to every affected host and review settings regularly.<ul><li>Disable unused services and change all default credentials.</li><li>Enable logging and monitor for unexpected changes.</li></ul></div></div>
    <div class="f-row assets"><div class="f-tag"><svg viewBox="0 0 8 8"><rect x="1" y="1.5" width="6" height="4" fill="none" stroke="#fff" stroke-width=".8"/><path d="M3 7h2M4 5.5V7" stroke="#fff" stroke-width=".8"/></svg>Assets Affected</div><div class="f-text"><ul><li>127.0.0.1</li><li>127.0.0.2</li><li>127.0.0.3</li></ul></div></div>
  </div>
  <div class="foot-edge"></div><div class="foot-left">Client Name Engagement Title</div>
  <div class="foot-right-edge"></div><div class="foot-right">6</div>
</section>

<section class="page">
  <div class="brand"><span class="brand-mark"></span><span class="brand-name">IRONQUILL</span></div>
  <div class="finding">
    <div class="f-head"><div class="f-name">Missing Patches</div><div class="f-sev-label">Severity</div><div class="f-sev crit">Critical</div></div>
    <div class="f-row obs"><div class="f-tag"><svg viewBox="0 0 8 8"><circle cx="3.3" cy="3.3" r="2.3" fill="none" stroke="#fff" stroke-width=".9"/><path d="M5 5l2.3 2.3" stroke="#fff" stroke-width="1"/></svg>Observation</div><div class="f-text">Several hosts run software without current patches, leaving known flaws open to attackers with public exploit code available.</div></div>
    <div class="f-row ev"><div class="f-tag"><svg viewBox="0 0 8 8"><rect x="1" y="2.5" width="6" height="4.5" fill="none" stroke="#fff" stroke-width=".8"/><path d="M3 2.5V1.5h2v1" fill="none" stroke="#fff" stroke-width=".8"/></svg>Evidence</div><div class="f-text"><div class="shot" role="img" aria-label="Screenshot of scan results"></div><p class="caption">Figure #1 - This is a caption for the above screenshot</p></div></div>
    <div class="f-row rec"><div class="f-tag"><svg viewBox="0 0 8 8"><rect x="1.5" y="1.2" width="5" height="6.3" fill="none" stroke="#fff" stroke-width=".8"/><path d="M2.8 3.3h2.4M2.8 4.7h2.4" stroke="#fff" stroke-width=".6"/></svg>Recommendation</div><div class="f-text">Set up a regular patch cycle and confirm updates are applied on each host.<ul><li>Prioritise patches for internet facing systems first.</li><li>Track missing updates in a central report.</li></ul></div></div>
    <div class="f-row assets"><div class="f-tag"><svg viewBox="0 0 8 8"><rect x="1" y="1.5" width="6" height="4" fill="none" stroke="#fff" stroke-width=".8"/><path d="M3 7h2M4 5.5V7" stroke="#fff" stroke-width=".8"/></svg>Assets Affected</div><div class="f-text"><ul><li>127.0.0.1</li><li>127.0.0.2</li><li>127.0.0.3</li></ul></div></div>
  </div>
  <div class="foot-edge"></div><div class="foot-left">Client Name Engagement Title</div>
  <div class="foot-right-edge"></div><div class="foot-right">7</div>
</section>

<section class="page">
  <div class="brand"><span class="brand-mark"></span><span class="brand-name">IRONQUILL</span></div>
  <div class="finding-title"><div class="h-small">HighFinding</div></div>
  <div class="finding">
    <div class="f-head"><div class="f-name">Insecure Configurations Identified</div><div class="f-sev-label">Severity</div><div class="f-sev high">High</div></div>
    <div class="f-row obs"><div class="f-tag"><svg viewBox="0 0 8 8"><circle cx="3.3" cy="3.3" r="2.3" fill="none" stroke="#fff" stroke-width=".9"/><path d="M5 5l2.3 2.3" stroke="#fff" stroke-width="1"/></svg>Observation</div><div class="f-text">Several hosts expose services with default settings, allowing unauthorised users to view sensitive details and change system behaviour.</div></div>
    <div class="f-row ev"><div class="f-tag"><svg viewBox="0 0 8 8"><rect x="1" y="2.5" width="6" height="4.5" fill="none" stroke="#fff" stroke-width=".8"/><path d="M3 2.5V1.5h2v1" fill="none" stroke="#fff" stroke-width=".8"/></svg>Evidence</div><div class="f-text"><div class="shot" role="img" aria-label="Screenshot of scan results"></div><p class="caption">Figure #1 - This is a caption for the above screenshot</p></div></div>
    <div class="f-row rec"><div class="f-tag"><svg viewBox="0 0 8 8"><rect x="1.5" y="1.2" width="5" height="6.3" fill="none" stroke="#fff" stroke-width=".8"/><path d="M2.8 3.3h2.4M2.8 4.7h2.4" stroke="#fff" stroke-width=".6"/></svg>Recommendation</div><div class="f-text">Apply a secure baseline to every affected host and review settings regularly.<ul><li>Disable unused services and change all default credentials.</li><li>Enable logging and monitor for unexpected changes.</li></ul></div></div>
    <div class="f-row assets"><div class="f-tag"><svg viewBox="0 0 8 8"><rect x="1" y="1.5" width="6" height="4" fill="none" stroke="#fff" stroke-width=".8"/><path d="M3 7h2M4 5.5V7" stroke="#fff" stroke-width=".8"/></svg>Assets Affected</div><div class="f-text"><ul><li>127.0.0.1</li><li>127.0.0.2</li><li>127.0.0.3</li></ul></div></div>
  </div>
  <div class="foot-edge"></div><div class="foot-left">Client Name Engagement Title</div>
  <div class="foot-right-edge"></div><div class="foot-right">8</div>
</section>

<section class="page">
  <div class="brand"><span class="brand-mark"></span><span class="brand-name">IRONQUILL</span></div>
  <div class="finding">
    <div class="f-head"><div class="f-name">Missing Patches</div><div class="f-sev-label">Severity</div><div class="f-sev high">High</div></div>
    <div class="f-row obs"><div class="f-tag"><svg viewBox="0 0 8 8"><circle cx="3.3" cy="3.3" r="2.3" fill="none" stroke="#fff" stroke-width=".9"/><path d="M5 5l2.3 2.3" stroke="#fff" stroke-width="1"/></svg>Observation</div><div class="f-text">Several hosts run software without current patches, leaving known flaws open to attackers with public exploit code available.</div></div>
    <div class="f-row ev"><div class="f-tag"><svg viewBox="0 0 8 8"><rect x="1" y="2.5" width="6" height="4.5" fill="none" stroke="#fff" stroke-width=".8"/><path d="M3 2.5V1.5h2v1" fill="none" stroke="#fff" stroke-width=".8"/></svg>Evidence</div><div class="f-text"><div class="shot" role="img" aria-label="Screenshot of scan results"></div><p class="caption">Figure #1 - This is a caption for the above screenshot</p></div></div>
    <div class="f-row rec"><div class="f-tag"><svg viewBox="0 0 8 8"><rect x="1.5" y="1.2" width="5" height="6.3" fill="none" stroke="#fff" stroke-width=".8"/><path d="M2.8 3.3h2.4M2.8 4.7h2.4" stroke="#fff" stroke-width=".6"/></svg>Recommendation</div><div class="f-text">Set up a regular patch cycle and confirm updates are applied on each host.<ul><li>Prioritise patches for internet facing systems first.</li><li>Track missing updates in a central report.</li></ul></div></div>
    <div class="f-row assets"><div class="f-tag"><svg viewBox="0 0 8 8"><rect x="1" y="1.5" width="6" height="4" fill="none" stroke="#fff" stroke-width=".8"/><path d="M3 7h2M4 5.5V7" stroke="#fff" stroke-width=".8"/></svg>Assets Affected</div><div class="f-text"><ul><li>127.0.0.1</li><li>127.0.0.2</li><li>127.0.0.3</li></ul></div></div>
  </div>
  <div class="foot-edge"></div><div class="foot-left">Client Name Engagement Title</div>
  <div class="foot-right-edge"></div><div class="foot-right">9</div>
</section>

<section class="page">
  <div class="brand"><span class="brand-mark"></span><span class="brand-name">IRONQUILL</span></div>
  <div class="finding-title"><div class="h-small">Medium Finding</div></div>
  <div class="finding">
    <div class="f-head"><div class="f-name">Insecure Configurations Identified</div><div class="f-sev-label">Severity</div><div class="f-sev med">Medium</div></div>
    <div class="f-row obs"><div class="f-tag"><svg viewBox="0 0 8 8"><circle cx="3.3" cy="3.3" r="2.3" fill="none" stroke="#fff" stroke-width=".9"/><path d="M5 5l2.3 2.3" stroke="#fff" stroke-width="1"/></svg>Observation</div><div class="f-text">Several hosts expose services with default settings, allowing unauthorised users to view sensitive details and change system behaviour.</div></div>
    <div class="f-row ev"><div class="f-tag"><svg viewBox="0 0 8 8"><rect x="1" y="2.5" width="6" height="4.5" fill="none" stroke="#fff" stroke-width=".8"/><path d="M3 2.5V1.5h2v1" fill="none" stroke="#fff" stroke-width=".8"/></svg>Evidence</div><div class="f-text"><div class="shot" role="img" aria-label="Screenshot of scan results"></div><p class="caption">Figure #1 - This is a caption for the above screenshot</p></div></div>
    <div class="f-row rec"><div class="f-tag"><svg viewBox="0 0 8 8"><rect x="1.5" y="1.2" width="5" height="6.3" fill="none" stroke="#fff" stroke-width=".8"/><path d="M2.8 3.3h2.4M2.8 4.7h2.4" stroke="#fff" stroke-width=".6"/></svg>Recommendation</div><div class="f-text">Apply a secure baseline to every affected host and review settings regularly.<ul><li>Disable unused services and change all default credentials.</li><li>Enable logging and monitor for unexpected changes.</li></ul></div></div>
    <div class="f-row assets"><div class="f-tag"><svg viewBox="0 0 8 8"><rect x="1" y="1.5" width="6" height="4" fill="none" stroke="#fff" stroke-width=".8"/><path d="M3 7h2M4 5.5V7" stroke="#fff" stroke-width=".8"/></svg>Assets Affected</div><div class="f-text"><ul><li>127.0.0.1</li><li>127.0.0.2</li><li>127.0.0.3</li></ul></div></div>
  </div>
  <div class="foot-edge"></div><div class="foot-left">Client Name Engagement Title</div>
  <div class="foot-right-edge"></div><div class="foot-right">10</div>
</section>

<section class="page">
  <div class="brand"><span class="brand-mark"></span><span class="brand-name">IRONQUILL</span></div>
  <div class="finding">
    <div class="f-head"><div class="f-name">Missing Hardening Check</div><div class="f-sev-label">Severity</div><div class="f-sev med">Medium</div></div>
    <div class="f-row obs"><div class="f-tag"><svg viewBox="0 0 8 8"><circle cx="3.3" cy="3.3" r="2.3" fill="none" stroke="#fff" stroke-width=".9"/><path d="M5 5l2.3 2.3" stroke="#fff" stroke-width="1"/></svg>Observation</div><div class="f-text">Hardening controls are missing on several servers, so weak protocols and open shares remain available to any network user.</div></div>
    <div class="f-row ev"><div class="f-tag"><svg viewBox="0 0 8 8"><rect x="1" y="2.5" width="6" height="4.5" fill="none" stroke="#fff" stroke-width=".8"/><path d="M3 2.5V1.5h2v1" fill="none" stroke="#fff" stroke-width=".8"/></svg>Evidence</div><div class="f-text"><div class="shot" role="img" aria-label="Screenshot of scan results"></div><p class="caption">Figure #1 - This is a caption for the above screenshot</p></div></div>
    <div class="f-row rec"><div class="f-tag"><svg viewBox="0 0 8 8"><rect x="1.5" y="1.2" width="5" height="6.3" fill="none" stroke="#fff" stroke-width=".8"/><path d="M2.8 3.3h2.4M2.8 4.7h2.4" stroke="#fff" stroke-width=".6"/></svg>Recommendation</div><div class="f-text">Adopt a recognised hardening guide and verify each server against it.<ul><li>Turn off legacy protocols and close open shares.</li><li>Audit settings after every major change.</li></ul></div></div>
    <div class="f-row assets"><div class="f-tag"><svg viewBox="0 0 8 8"><rect x="1" y="1.5" width="6" height="4" fill="none" stroke="#fff" stroke-width=".8"/><path d="M3 7h2M4 5.5V7" stroke="#fff" stroke-width=".8"/></svg>Assets Affected</div><div class="f-text"><ul><li>127.0.0.1</li><li>127.0.0.2</li><li>127.0.0.3</li></ul></div></div>
  </div>
  <div class="foot-edge"></div><div class="foot-left">Client Name Engagement Title</div>
  <div class="foot-right-edge"></div><div class="foot-right">11</div>
</section>

<section class="page">
  <div class="brand"><span class="brand-mark"></span><span class="brand-name">IRONQUILL</span></div>
  <div class="finding-title"><div class="h-small">Low Finding</div></div>
  <div class="finding">
    <div class="f-head"><div class="f-name">Insecure Configurations Identified</div><div class="f-sev-label">Severity</div><div class="f-sev low">Low</div></div>
    <div class="f-row obs"><div class="f-tag"><svg viewBox="0 0 8 8"><circle cx="3.3" cy="3.3" r="2.3" fill="none" stroke="#fff" stroke-width=".9"/><path d="M5 5l2.3 2.3" stroke="#fff" stroke-width="1"/></svg>Observation</div><div class="f-text">Several hosts expose services with default settings, allowing unauthorised users to view sensitive details and change system behaviour.</div></div>
    <div class="f-row ev"><div class="f-tag"><svg viewBox="0 0 8 8"><rect x="1" y="2.5" width="6" height="4.5" fill="none" stroke="#fff" stroke-width=".8"/><path d="M3 2.5V1.5h2v1" fill="none" stroke="#fff" stroke-width=".8"/></svg>Evidence</div><div class="f-text"><div class="shot" role="img" aria-label="Screenshot of scan results"></div><p class="caption">Figure #1 - This is a caption for the above screenshot</p></div></div>
    <div class="f-row rec"><div class="f-tag"><svg viewBox="0 0 8 8"><rect x="1.5" y="1.2" width="5" height="6.3" fill="none" stroke="#fff" stroke-width=".8"/><path d="M2.8 3.3h2.4M2.8 4.7h2.4" stroke="#fff" stroke-width=".6"/></svg>Recommendation</div><div class="f-text">Apply a secure baseline to every affected host and review settings regularly.<ul><li>Disable unused services and change all default credentials.</li><li>Enable logging and monitor for unexpected changes.</li></ul></div></div>
    <div class="f-row assets"><div class="f-tag"><svg viewBox="0 0 8 8"><rect x="1" y="1.5" width="6" height="4" fill="none" stroke="#fff" stroke-width=".8"/><path d="M3 7h2M4 5.5V7" stroke="#fff" stroke-width=".8"/></svg>Assets Affected</div><div class="f-text"><ul><li>127.0.0.1</li><li>127.0.0.2</li><li>127.0.0.3</li></ul></div></div>
  </div>
  <div class="foot-edge"></div><div class="foot-left">Client Name Engagement Title</div>
  <div class="foot-right-edge"></div><div class="foot-right">12</div>
</section>

<section class="page">
  <div class="brand"><span class="brand-mark"></span><span class="brand-name">IRONQUILL</span></div>
  <div class="finding">
    <div class="f-head"><div class="f-name">Missing Hardening Check</div><div class="f-sev-label">Severity</div><div class="f-sev low">Low</div></div>
    <div class="f-row obs"><div class="f-tag"><svg viewBox="0 0 8 8"><circle cx="3.3" cy="3.3" r="2.3" fill="none" stroke="#fff" stroke-width=".9"/><path d="M5 5l2.3 2.3" stroke="#fff" stroke-width="1"/></svg>Observation</div><div class="f-text">Hardening controls are missing on several servers, so weak protocols and open shares remain available to any network user.</div></div>
    <div class="f-row ev"><div class="f-tag"><svg viewBox="0 0 8 8"><rect x="1" y="2.5" width="6" height="4.5" fill="none" stroke="#fff" stroke-width=".8"/><path d="M3 2.5V1.5h2v1" fill="none" stroke="#fff" stroke-width=".8"/></svg>Evidence</div><div class="f-text"><div class="shot" role="img" aria-label="Screenshot of scan results"></div><p class="caption">Figure #1 - This is a caption for the above screenshot</p></div></div>
    <div class="f-row rec"><div class="f-tag"><svg viewBox="0 0 8 8"><rect x="1.5" y="1.2" width="5" height="6.3" fill="none" stroke="#fff" stroke-width=".8"/><path d="M2.8 3.3h2.4M2.8 4.7h2.4" stroke="#fff" stroke-width=".6"/></svg>Recommendation</div><div class="f-text">Adopt a recognised hardening guide and verify each server against it.<ul><li>Turn off legacy protocols and close open shares.</li><li>Audit settings after every major change.</li></ul></div></div>
    <div class="f-row assets"><div class="f-tag"><svg viewBox="0 0 8 8"><rect x="1" y="1.5" width="6" height="4" fill="none" stroke="#fff" stroke-width=".8"/><path d="M3 7h2M4 5.5V7" stroke="#fff" stroke-width=".8"/></svg>Assets Affected</div><div class="f-text"><ul><li>127.0.0.1</li><li>127.0.0.2</li><li>127.0.0.3</li></ul></div></div>
  </div>
  <div class="foot-edge"></div><div class="foot-left">Client Name Engagement Title</div>
  <div class="foot-right-edge"></div><div class="foot-right">13</div>
</section>

<!-- appendix -->
<section class="page">
  <div class="brand"><span class="brand-mark"></span><span class="brand-name">IRONQUILL</span></div>
  <div class="body">
    <h1 class="h-red" style="margin-bottom:0">Appendix 01</h1>
    <h2 class="h-dark">Engagement Methodology</h2>
    <p class="para">Testing followed a phased approach of discovery, enumeration, exploitation and reporting, aligned with recognised industry frameworks and the agreed rules of engagement for this assessment.</p>
  </div>
  <div class="foot-edge"></div><div class="foot-left">Client Name Engagement Title</div>
  <div class="foot-right-edge"></div><div class="foot-right">14</div>
</section>

<!-- contact -->
<section class="page">
  <div class="brand"><span class="brand-mark"></span><span class="brand-name">IRONQUILL</span></div>
  <div class="body"><h1 class="h-red">Our Contact</h1></div>
  <div class="contact-photo" role="img" aria-label="Laptop on a bright office desk"></div>
  <div class="contact-list">
    <div class="contact-item"><span class="c-icon"><svg viewBox="0 0 4 4"><path d="M2 .3a1.2 1.2 0 0 1 1.2 1.2C3.2 2.4 2 3.7 2 3.7S.8 2.4.8 1.5A1.2 1.2 0 0 1 2 .3z" fill="#fff"/></svg></span><div><div class="c-label">Address</div><div class="c-value">48 Harbour Lane, Westport 20410</div></div></div>
    <div class="contact-item"><span class="c-icon"><svg viewBox="0 0 4 4"><path d="M.6.5h1l.4 1-.6.4a2 2 0 0 0 .8.8l.4-.6 1 .4v1C2 3.6.4 2 .6.5z" fill="#fff"/></svg></span><div><div class="c-label">Phone</div><div class="c-value">555-014-2290</div></div></div>
    <div class="contact-item"><span class="c-icon"><svg viewBox="0 0 4 4"><rect x=".4" y="1" width="3.2" height="2.2" fill="none" stroke="#fff" stroke-width=".4"/><path d="M.4 1l1.6 1.2L3.6 1" fill="none" stroke="#fff" stroke-width=".4"/></svg></span><div><div class="c-label">Email</div><div class="c-value">contact@ironquill.com</div></div></div>
    <div class="contact-item"><span class="c-icon"><svg viewBox="0 0 4 4"><rect x=".4" y=".7" width="3.2" height="2" fill="none" stroke="#fff" stroke-width=".4"/><path d="M1.3 3.4h1.4" stroke="#fff" stroke-width=".4"/></svg></span><div><div class="c-label">Website</div><div class="c-value">www.ironquill.com</div></div></div>
  </div>
  <div class="foot-edge"></div><div class="foot-left">Client Name Engagement Title</div>
  <div class="foot-right-edge"></div><div class="foot-right">15</div>
</section>

</main>
</body>
</html>
```